Auto Dealership needs a exterior sign

We need a sign design for an exterior sign that measures 10 Ft wide and 4 ft tall. The sign needs to say, "Tarn Motors" in large lettering and the address," 718 North Birch Avenue Corvell, Idaho 84971 needs to be below the lettering "Tarn Motors" Also the lettering "Dealer #" needs to be in the sign somewhere, preferable a lower corner. We would like the theme of the sign to be graphics associated with the San Rafael Swell in Utah. I will upload a a few graphics. I would prefer a graphic of Delicate Arch in Arches nation Park to be in the background of the sign. Colors are Red, White, Black, Tan and possible Blue or Yellow.

Here are a couple more ideas for what I am looking for. Simple design, solid back ground blue or red.Please look at attachment for my ideas. I want something similar to the pic of the velmox sign. Matbe the same font. With the arch in tan or brown. Added Friday, May 27, 2016

Reason: Have not had time to review and send feedback.

Target Market(s)

Buyers of cars, trucks, Powersports, Recreational vehicles, Motorcycles

Industry/Entity Type

Automotive

Colors
f04a51
0355a3
fbed22
ffffff
cadf82

Requirements
Must have
• A Large Border, with large font lettering and the lettering must have an outline that highlights the wording with preferable a bubbly font. Here is the wording,
• "Tarn Motors"
• 718 North Birch Avenue
• Corvell, Idaho 84971
• Dealer# 435-218-5937
• Autos Powersports Recreation
Nice to have
• I really want to use a Graphic of Delicate Arch in Utah as a background Graphic that can be on the side or in the middle. preferable extra large in the middle with the wording in front of it. Possible a Dark Red Sign or a Dark Blue Sign. Most important is the contrast between the signage and the lettering. It needs to really stick out.

```html
<!DOCTYPE html>
<html lang="en">
<head>
<meta charset="utf-8">
<title>Tarn Motors – Exterior Sign</title>
<link rel="stylesheet" href="https://fonts.googleapis.com/css2?family=Archivo:ital,wdth,wght@0,62..125,400..900;1,62..125,400..900&display=swap">
<style>
  :root {
    --page: #c0bebe;
    --sky: #0355a3;
    --yellow: #f3ec25;
    --white: #ffffff;
    --earth-dark: #472b1b;
    --rock: #d4572a;
    --rock-deep: #b7441f;
    --rock-light: #e26b34;
    --ink: #3d2617;
    --shadow: #3a2314;
  }
  html, body {
    margin: 0;
    padding: 0;
    width: 1200px;
    height: 720px;
    overflow: hidden;
    background: var(--page);
  }
  .sign {
    position: absolute;
    left: 0;
    top: 120px;
    width: 1200px;
    height: 480px;
    background: var(--sky);
    overflow: hidden;
    font-family: "Archivo", "Arial", sans-serif;
  }
  .landscape {
    position: absolute;
    left: 0;
    top: 303px;
    width: 1200px;
    height: 177px;
    background: linear-gradient(to bottom, var(--earth-dark) 0%, var(--earth-dark) 34%, var(--rock-deep) 38%, var(--rock) 70%, var(--rock-deep) 100%);
  }
  .arch {
    position: absolute;
    left: 751px;
    top: 58px;
    width: 413px;
    height: 422px;
    background: linear-gradient(160deg, var(--rock-light) 0%, var(--rock) 55%, var(--rock-deep) 100%);
  }
  .brand-name,
  .brand-sub {
    position: absolute;
    margin: 0;
    font-weight: 900;
    font-style: normal;
    font-stretch: 110%;
    line-height: 1;
    color: var(--yellow);
  }
  .brand-name {
    right: 463px;
    top: 46px;
    font-size: 128px;
    letter-spacing: -2px;
  }
  .brand-sub {
    right: 472px;
    top: 160px;
    font-size: 60px;
    letter-spacing: -1px;
  }
  .tagline {
    position: absolute;
    right: 479px;
    top: 226px;
    margin: 0;
    font-size: 36px;
    font-weight: 800;
    font-style: italic;
    font-stretch: 62%;
    line-height: 1;
    color: var(--yellow);
    white-space: nowrap;
  }
  .address {
    position: absolute;
    right: 487px;
    top: 270px;
    margin: 0;
    font-size: 17px;
    font-weight: 400;
    line-height: 1;
    letter-spacing: 0.2px;
    color: var(--white);
    white-space: nowrap;
  }
  .dealer-band {
    position: absolute;
    left: 0;
    top: 399px;
    width: 470px;
    height: 48px;
  }
  .dealer-text {
    position: absolute;
    left: 50px;
    top: 406px;
    margin: 0;
    color: var(--ink);
    line-height: 1;
    white-space: nowrap;
  }
  .dealer-label {
    font-size: 28px;
    font-weight: 500;
    font-stretch: 88%;
    margin-right: 18px;
  }
  .dealer-phone {
    font-size: 34px;
    font-weight: 700;
    font-stretch: 82%;
  }
</style>
</head>
<body>
  <main class="sign">
    <div class="landscape" role="img" aria-label="Red rock desert landscape with dark mesa horizon"></div>
    <div class="arch" role="img" aria-label="Illustration of Delicate Arch in red-orange sandstone"></div>

    <h1 class="brand-name">TARN</h1>
    <p class="brand-sub">MOTORS</p>
    <p class="tagline">AUTOS POWERSPORTS RECREATION</p>
    <p class="address">718 NORTH BIRCH AVENUE, CORVELL, IDAHO 84971</p>

    <svg class="dealer-band" viewBox="0 0 470 48" aria-hidden="true">
      <polygon points="0,6 470,6 438,48 0,48" fill="var(--shadow)"/>
      <polygon points="0,0 468,0 436,42 0,42" fill="var(--white)"/>
    </svg>
    <p class="dealer-text"><span class="dealer-label">DEALER#</span><span class="dealer-phone">435-218-5937</span></p>
  </main>
</body>
</html>
```